Brenmoor Group needs a business card

I would like the card to be simple but modern and elegant.
I like black and white.
or black and gold.
we are a private finance lender and also are involved in property and property developments.

please look at the business card photos i provided i would like B.G only one one side and all the other details on the other side use fonts that tie in with my theme.

Industry/Entity Type

Finance

Contact Information for Business Card

Brenmoor Group (B.G) Callum Brenmoor M: 0418396152 E: callumbren@quivomail.com

Font styles to use
Other font styles liked:
• Use fonts that would reflect our business

Colors
000000
ffffff

Requirements
Must have
• one side of details
• other side has either B.G or Brenmoor Group like in the photos provided

```html
<!DOCTYPE html>
<html lang="en">
<head>
<meta charset="utf-8">
<title>Brenmoor Group — Business Card</title>
<link rel="stylesheet" href="https://fonts.googleapis.com/css2?family=Lexend:wght@300;400;600&display=swap">
<style>
  :root {
    --ink: #000000;
    --paper: #ffffff;
    --backdrop: #dcdde0;
    --edge: rgba(0, 0, 0, 0.08);
  }
  * { margin: 0; padding: 0; box-sizing: border-box; }
  html, body {
    width: 1200px;
    height: 800px;
    overflow: hidden;
    background: var(--backdrop);
    font-family: "Lexend", "Helvetica Neue", Arial, sans-serif;
    color: var(--ink);
  }
  .canvas {
    position: relative;
    width: 1200px;
    height: 800px;
    display: flex;
    align-items: center;
    justify-content: center;
    gap: 60px;
  }
  .card {
    position: relative;
    width: 500px;
    height: 286px;
    background: var(--paper);
    box-shadow: 0 1px 2px var(--edge), 0 10px 28px rgba(0, 0, 0, 0.08);
  }

  /* Details side */
  .card--details .company {
    position: absolute;
    left: 64px;
    top: 52px;
    font-weight: 300;
    font-size: 17px;
    letter-spacing: 0.06em;
    text-transform: uppercase;
    white-space: nowrap;
  }
  .card--details .company-rule {
    position: absolute;
    left: 64px;
    top: 82px;
    width: 228px;
    height: 1.5px;
    background: var(--ink);
  }
  .card--details .contact {
    position: absolute;
    left: 64px;
    top: 140px;
    text-transform: uppercase;
    white-space: nowrap;
  }
  .contact .person {
    font-weight: 600;
    font-size: 16px;
    letter-spacing: 0.05em;
    margin-bottom: 8px;
  }
  .contact .line {
    font-weight: 300;
    font-size: 13px;
    letter-spacing: 0.04em;
    line-height: 1.9;
  }

  /* Name side */
  .card--name {
    display: flex;
    align-items: center;
    justify-content: center;
  }
  .brand {
    display: flex;
    align-items: center;
    gap: 16px;
  }
  .brand-mark {
    width: 14px;
    height: 14px;
    background: var(--ink);
  }
  .brand-name {
    font-weight: 400;
    font-size: 30px;
    letter-spacing: 0.04em;
    white-space: nowrap;
  }
</style>
</head>
<body>
  <main class="canvas">
    <section class="card card--details" aria-label="Business card, details side">
      <p class="company">Brenmoor Group (B.G)</p>
      <div class="company-rule"></div>
      <div class="contact">
        <p class="person">Callum Brenmoor</p>
        <p class="line">M: 0418396152</p>
        <p class="line">E: callumbren@quivomail.com</p>
      </div>
    </section>

    <section class="card card--name" aria-label="Business card, name side">
      <div class="brand">
        <span class="brand-mark"></span>
        <p class="brand-name">Brenmoor Group</p>
      </div>
    </section>
  </main>
</body>
</html>
```